Vivaform - Fitness Coach. Needs a Business Card Design that I can also use for other advertising

Established 2012, I have finished the QPLB National Certificate in Fitness & Personal Training. Harrowgate First Aid Certificate. I have the Auckland 800m track records for MW45. I also came 1st at the 2012 Pacifica Games in 800 & 1500m. I am passionate about health & fitness and would like to help people reach their health & fitness goals. I also take health & fitness weekends. Main interests - Running, Weight Training, Yoga & Aqua Jogging. I like strength/power, but am femine.

Target Market(s)

Male or Female 18 and over that wants to improve their health & fitness

Industry/Entity Type

Advertising

Requirements
Must have
• my name: Lorissa K Dunmore contact details: lori@brightpath.co.nz mobile - 021 579318 URL name: facebook.com/lorissaKdunmore - VivaForm
Photo of Me

```html
<!DOCTYPE html>
<html lang="en">
<head>
<meta charset="UTF-8">
<title>VivaForm Business Card</title>
<link rel="stylesheet" href="https://fonts.googleapis.com/css2?family=Jost:wght@400;600;700&display=swap">
<style>
  :root {
    --page-bg: #e9e9e9;
    --leaf-dark: #2f4a22;
    --leaf-mid: #4d6e34;
    --lawn: #7fae48;
    --tank-orange: #e8813e;
    --tights-grey: #3d3f45;
    --faded-leaf: #c9cfc4;
    --faded-light: #dfe3db;
    --faded-orange: #e9c3a4;
    --faded-grey: #a9aca8;
    --ink: #111111;
    --ink-soft: #333333;
    --white: #ffffff;
  }
  * { box-sizing: border-box; margin: 0; padding: 0; }
  html, body {
    width: 1067px;
    height: 1200px;
    overflow: hidden;
    background: var(--page-bg);
    font-family: "Jost", sans-serif;
  }
  .sheet {
    position: relative;
    width: 1067px;
    height: 1200px;
  }
  .card {
    position: absolute;
    left: 103px;
    width: 860px;
    height: 525px;
    overflow: hidden;
    box-shadow: 0 6px 18px rgba(0,0,0,0.25);
  }
  .card--front { top: 50px; }
  .card--back { top: 625px; }

  .card__backdrop {
    position: absolute;
    inset: 0;
  }
  .card--front .card__backdrop {
    background:
      linear-gradient(180deg, transparent 74%, var(--lawn) 100%),
      radial-gradient(ellipse at 60% 45%, var(--leaf-mid) 0%, var(--leaf-dark) 75%);
  }
  .card--back .card__backdrop {
    background: linear-gradient(160deg, var(--faded-leaf) 0%, #d3d8cd 60%, #cdd3c7 100%);
  }

  .front__jump-sequence {
    position: absolute;
    left: 250px;
    top: 70px;
    width: 560px;
    height: 330px;
    border-radius: 18px;
    background:
      linear-gradient(180deg, rgba(232,129,62,0.85) 0%, rgba(232,129,62,0.75) 40%, rgba(61,63,69,0.85) 62%, rgba(61,63,69,0.75) 100%);
  }

  .back__jump-photo {
    position: absolute;
    left: 500px;
    top: 30px;
    width: 300px;
    height: 440px;
    border-radius: 18px;
    background:
      linear-gradient(180deg, rgba(233,195,164,0.9) 0%, rgba(233,195,164,0.8) 42%, rgba(169,172,168,0.85) 62%, rgba(169,172,168,0.7) 100%);
  }

  .front__wordmark {
    position: absolute;
    right: 44px;
    bottom: 62px;
    color: var(--white);
    font-weight: 700;
    font-size: 72px;
    letter-spacing: 1px;
    line-height: 1;
  }

  .back__details {
    position: absolute;
    left: 70px;
    top: 95px;
    color: var(--ink);
  }
  .back__wordmark {
    font-weight: 700;
    font-size: 66px;
    letter-spacing: 1px;
    line-height: 1;
  }
  .back__name {
    margin-top: 70px;
    margin-left: 40px;
    font-weight: 700;
    font-size: 30px;
  }
  .contact {
    list-style: none;
    margin-top: 14px;
    margin-left: 120px;
    font-size: 20px;
    line-height: 1.9;
    font-weight: 400;
  }
  .contact__label { color: var(--ink-soft); }
  .contact strong { font-weight: 600; }
</style>
</head>
<body>
  <main class="sheet">
    <section class="card card--front">
      <div class="card__backdrop" role="img" aria-label="Green leafy hedge above a lawn"></div>
      <div class="front__jump-sequence" role="img" aria-label="Photo sequence of the coach in an orange top jumping in front of the hedge"></div>
      <div class="front__wordmark">VivaForm</div>
    </section>

    <section class="card card--back">
      <div class="card__backdrop" role="img" aria-label="Faded leafy hedge"></div>
      <div class="back__jump-photo" role="img" aria-label="Faded photo of the coach jumping"></div>
      <div class="back__details">
        <div class="back__wordmark">VivaForm</div>
        <p class="back__name">Lorissa K Dunmore</p>
        <ul class="contact">
          <li><span class="contact__label">email:</span> <strong>lori@brightpath.co.nz</strong></li>
          <li><span class="contact__label">mobile:</span> <strong>021 579318</strong></li>
          <li><span class="contact__label">facebook/</span><strong>Vivaform</strong></li>
        </ul>
      </div>
    </section>
  </main>
</body>
</html>
```